Dental Office Needs- Flyer Design for Same Day Crowns

We need a flyer that will explain the benefits of the same day crown from the patient prospective. Not show pictures of the machine that makes the crowns. See attached material for content. The flyer should use the practices PMS colors of Green 562 and Blue 3025. The ad should say to the patient - I want to go this office and get my crown done there.
Updates

Project Deadline Extended Reason: The difference in the time zone between USA and Europe has caused issues. Minor changes still need to be worked out. Added Thursday, July 14, 2016

Target Market(s)

Dental Patients

Industry/Entity Type

Dental

Requirements
Must have
• Call to Action
• Business Address and Business Logo
• Classic Design
• images of a Happy 50 year old Couple
• Gives the benefits of the same day crown
Should not have
• No Images of tooth figures
• No before or after pictures

```html
<!DOCTYPE html>
<html lang="en">
<head>
<meta charset="utf-8">
<title>Brookside Dental Care – One Visit Crowns</title>
<link href="https://fonts.googleapis.com/css2?family=Fira+Sans:wght@300;400;600;700&family=Fira+Sans+Condensed:wght@600;700&family=Roboto+Condensed:wght@700&display=swap" rel="stylesheet">
<style>
  :root{
    --blue:#045a8d;
    --blue-line:#5f9bc8;
    --green:#4aa73e;
    --green-text:#3fa23a;
    --sky-top:#d9f1fb;
    --sky-low:#c4e6f7;
    --panel-light:#cde8f9;
    --grey-text:#7d7d7d;
    --white:#ffffff;
  }
  html,body{margin:0;padding:0;width:941px;height:1200px;overflow:hidden;background:var(--white);}
  .flyer{position:relative;width:941px;height:1200px;font-family:"Fira Sans",sans-serif;}
  .flyer-shapes{position:absolute;left:0;top:0;}
  .benefits{position:absolute;left:84px;top:116px;margin:0;padding:0;list-style:none;}
  .benefit{margin-bottom:44px;}
  .benefit:nth-child(2){margin-bottom:38px;}
  .benefit-head{display:flex;align-items:center;font-family:"Fira Sans Condensed",sans-serif;font-weight:700;font-size:43px;line-height:1;color:var(--green-text);}
  .benefit-head svg{margin-right:6px;}
  .benefit-sub{margin:2px 0 0 46px;font-family:"Fira Sans Condensed",sans-serif;font-weight:600;font-size:25px;line-height:30px;color:var(--green-text);}
  .intro{position:absolute;left:116px;top:770px;width:320px;margin:0;color:var(--white);font-weight:600;font-size:15.5px;line-height:21.5px;}
  .address{position:absolute;left:116px;top:878px;width:296px;margin:0;text-align:center;color:var(--white);font-weight:600;font-size:15.5px;line-height:21.5px;font-style:normal;}
  .brand-card{position:absolute;left:108px;top:982px;width:312px;height:134px;background:var(--white);box-shadow:0 2px 4px rgba(0,0,0,.35);display:flex;align-items:center;justify-content:center;gap:10px;}
  .brand-mark{width:14px;height:14px;border-radius:50%;background:var(--blue);}
  .brand-name{font-weight:600;font-size:24px;color:var(--blue);}
  .details{position:absolute;left:518px;top:770px;width:330px;color:var(--grey-text);font-weight:300;font-size:16px;line-height:21.5px;}
  .details p{margin:0 0 22px;}
  .cta{position:absolute;left:496px;top:1022px;width:362px;height:148px;background:var(--blue);border-radius:18px 18px 0 0;color:var(--white);text-align:center;}
  .cta-label{margin:20px 0 0;font-weight:700;font-size:30px;line-height:1;}
  .cta-phone{margin:6px 0 0;font-family:"Roboto Condensed",sans-serif;font-weight:700;font-size:52px;line-height:1;letter-spacing:-1px;}
  .cta-web{margin:10px 0 0;font-weight:700;font-size:14.5px;}
</style>
</head>
<body>
<div class="flyer">
  <svg class="flyer-shapes" width="941" height="1200" viewBox="0 0 941 1200">
    <defs>
      <linearGradient id="sky" x1="0" y1="0" x2="0" y2="1">
        <stop offset="0" stop-color="var(--sky-top)"/>
        <stop offset="1" stop-color="var(--sky-low)"/>
      </linearGradient>
      <linearGradient id="photo-tone" x1="0" y1="0" x2="1" y2="1">
        <stop offset="0" stop-color="#c8d3da"/>
        <stop offset="0.55" stop-color="#6f7a88"/>
        <stop offset="1" stop-color="#d6ccbd"/>
      </linearGradient>
      <clipPath id="panel"><rect x="30" y="30" width="880" height="1140"/></clipPath>
      <clipPath id="circle"><ellipse cx="470" cy="298" rx="470" ry="454"/></clipPath>
    </defs>
    <g clip-path="url(#panel)">
      <rect class="panel-bg" x="30" y="30" width="880" height="1140" fill="var(--panel-light)"/>
      <path class="panel-green-left" d="M30 808 C140 830 100 1000 130 1090 C180 1150 360 1110 470 1130 L470 1170 L30 1170 Z" fill="var(--green)"/>
      <path class="panel-green-right" d="M910 920 C840 960 800 1010 760 1030 L910 1030 Z" fill="var(--green)"/>
      <path class="info-column" d="M84 482 H444 V1116 Q444 1136 424 1136 H104 Q84 1136 84 1116 Z" fill="var(--blue)"/>
      <ellipse class="circle-band" cx="470" cy="300" rx="484" ry="460" fill="var(--blue)"/>
      <ellipse class="circle-line" cx="470" cy="298" rx="474" ry="457" fill="var(--blue-line)"/>
      <rect class="sky-top" x="30" y="30" width="880" height="268" fill="var(--sky-top)"/>
      <ellipse class="sky" cx="470" cy="298" rx="470" ry="454" fill="url(#sky)"/>
      <g clip-path="url(#circle)">
        <rect role="img" aria-label="Photo of a smiling, happy couple in their fifties outdoors" x="430" y="150" width="480" height="610" fill="url(#photo-tone)" opacity="0.85"/>
      </g>
    </g>
  </svg>

  <ul class="benefits">
    <li class="benefit">
      <div class="benefit-head"><svg width="38" height="34" viewBox="0 0 38 34"><path d="M2 19 L8 13 L15 21 L32 2 L37 7 L15 32 Z" fill="var(--green-text)"/></svg>GOOD-BYE</div>
      <div class="benefit-sub">TEMPORARY CROWN</div>
    </li>
    <li class="benefit">
      <div class="benefit-head"><svg width="38" height="34" viewBox="0 0 38 34"><path d="M2 19 L8 13 L15 21 L32 2 L37 7 L15 32 Z" fill="var(--green-text)"/></svg>GOOD-BYE</div>
      <div class="benefit-sub">SECOND APPOINTMENT</div>
    </li>
    <li class="benefit">
      <div class="benefit-head"><svg width="38" height="34" viewBox="0 0 38 34"><path d="M2 19 L8 13 L15 21 L32 2 L37 7 L15 32 Z" fill="var(--green-text)"/></svg>GOOD-BYE</div>
      <div class="benefit-sub">GOOEY MESSY<br>IMPRESSIONS</div>
    </li>
  </ul>

  <p class="intro">Brookside Dental Care is pleased to offer<br>you the Comfort and Convenience of<br>One Visit Dental Care.</p>
  <address class="address">418 N. Maple Avenue<br>Ashford, MI.</address>

  <div class="brand-card">
    <span class="brand-mark"></span>
    <span class="brand-name">Brookside Dental Care</span>
  </div>

  <div class="details">
    <p>Restorative Dentistry has evolved and<br>now, digital technology allows us to take<br>an impression of your teeth with a digital<br>scanner and create your restoration right<br>in our office.</p>
    <p>When it comes to your next crown,<br>the benefits of a Digital Restoration<br>add up quickly!</p>
  </div>

  <div class="cta">
    <p class="cta-label">CALL US TODAY</p>
    <p class="cta-phone">555.014.2290</p>
    <p class="cta-web">WWW.BROOKSIDEDENTALCARE.COM</p>
  </div>
</div>
</body>
</html>
```